Wendell's UPDATE -Across the Board

Insurance Agent Business card and probably everything else !
Been in business for over 35 years and never took the time to update so really like the black-gold combo but open for suggestions (Honestly, I have NO idea how this works but sounds very cool ) Attached are two samples that I enjoy. The black and gold option is my favorite so looking for something like that!

```html
<!DOCTYPE html>
<html lang="en">
<head>
<meta charset="utf-8">
<title>Wendell S Hartwell – Business Card</title>
<link rel="stylesheet" href="https://fonts.googleapis.com/css2?family=Montserrat:wght@400;500&family=Tinos:wght@700&display=swap">
<style>
  :root {
    --bg: #2a2a2a;
    --card: #1c1c1c;
    --card-edge: #232323;
    --gold: #c9a24f;
    --gold-light: #e2c47c;
  }
  * { margin: 0; padding: 0; box-sizing: border-box; }
  html, body { width: 1200px; height: 900px; overflow: hidden; }
  body {
    background: radial-gradient(circle at 60% 40%, #383838 0%, var(--bg) 55%, #151515 100%);
    position: relative;
    font-family: "Montserrat", sans-serif;
  }
  .card {
    position: absolute;
    left: 310px;
    width: 580px;
    height: 331px;
    background: linear-gradient(135deg, var(--card) 0%, var(--card-edge) 100%);
    box-shadow: 0 12px 30px rgba(0,0,0,0.55);
  }
  .card--front { top: 70px; }
  .card--back { top: 470px; }

  .brand {
    position: absolute;
    top: 50%; left: 50%;
    transform: translate(-50%, -50%);
    display: flex;
    align-items: center;
    gap: 14px;
    white-space: nowrap;
  }
  .brand__mark {
    width: 18px;
    height: 18px;
    background: var(--gold);
  }
  .brand__name {
    font-family: "Montserrat", sans-serif;
    font-weight: 500;
    font-size: 28px;
    color: var(--gold);
  }

  .identity {
    position: absolute;
    right: 280px;
    top: 112px;
    text-align: right;
    color: var(--gold);
    white-space: nowrap;
  }
  .identity__name {
    font-family: "Tinos", serif;
    font-weight: 700;
    font-size: 22px;
    letter-spacing: 0.5px;
    color: var(--gold-light);
    line-height: 1.2;
  }
  .identity__role,
  .identity__est {
    font-size: 15px;
    line-height: 1.3;
  }
  .divider {
    position: absolute;
    left: 320px;
    top: 100px;
    width: 1.5px;
    height: 140px;
    background: var(--gold);
  }
  .contact {
    position: absolute;
    left: 340px;
    top: 100px;
    color: var(--gold-light);
    font-size: 15px;
    line-height: 1.35;
    white-space: nowrap;
  }
  .contact__address { margin-bottom: 8px; }
  .contact__line { display: flex; align-items: center; gap: 8px; }
  .contact__line svg { width: 12px; height: 12px; flex: none; }
</style>
</head>
<body>
  <section class="card card--front" aria-label="Card front">
    <div class="brand">
      <span class="brand__mark" aria-hidden="true"></span>
      <span class="brand__name">Hartwell Insurance</span>
    </div>
  </section>

  <section class="card card--back" aria-label="Card back">
    <div class="identity">
      <div class="identity__name">WENDELL S HARTWELL</div>
      <div class="identity__role">Insurance &amp; Financial Consultant</div>
      <div class="identity__est">Est. 1985</div>
    </div>
    <div class="divider"></div>
    <div class="contact">
      <div class="contact__address">4120 Harbor Avenue,<br>Suite 210-3 Palm Vale,<br>FL 33065</div>
      <div class="contact__line">
        <svg viewBox="0 0 12 12" aria-hidden="true"><path d="M2.5 1 L4.5 1 L5.2 3.5 L4 4.5 Q5 7 7.5 8 L8.5 6.8 L11 7.5 L11 9.5 Q10 11 8 10.5 Q2 8.5 1 3 Q1 1.5 2.5 1 Z" fill="#e2c47c"/></svg>
        <span>555-210-4837</span>
      </div>
      <div class="contact__line">
        <svg viewBox="0 0 12 12" aria-hidden="true"><rect x="3" y="0.8" width="6" height="10.4" rx="1" fill="none" stroke="#e2c47c" stroke-width="1.2"/><rect x="5" y="9" width="2" height="1" fill="#e2c47c"/></svg>
        <span>555-210-7719</span>
      </div>
      <div class="contact__line">
        <svg viewBox="0 0 12 12" aria-hidden="true"><rect x="0.8" y="2.5" width="10.4" height="7" fill="none" stroke="#e2c47c" stroke-width="1.1"/><path d="M1 3 L6 7 L11 3" fill="none" stroke="#e2c47c" stroke-width="1.1"/></svg>
        <span>wendell@wshinsures.com</span>
      </div>
    </div>
  </section>
</body>
</html>
```